Cruise Booking Website

Cruise search and booking website

This project is a redesign of a cruise booking website we did a few years ago.

The current website is located here: http://voyage.pixelmarsh.com/en/

It's not fully functional but gives you ad idea how miserable the old design was.

All the information about cruises, cruise lines, destinations, ports and shore excursions will be similar to http://www.sailorbay.com/
Actual search pages (form, results, single result, sailing and cabin selection, ship info, booking) will have EXACTLY the same info as sailorbay.com

We like the style of http://harborvoyagehub.com, it's quite modern, good spacing, not overloaded with information. So you can use it as an example of what we like, not what we want as a final result for us. Please, don't copy it. The result should not be possible to resemble the harborvoyagehub.com, because our site has to be unique. This is important!
If you submit a design that clearly reminds another cruise site it will be rejected!

Also the mockup provided is just to give you the basic structure and show what information has to be present on the page. It doesn't mean the layout has to be the same as a mockup. The layout is up to the designer.

I've updated the mockup to be more generic so it doesn't confuse you:
https://www.filecrate.net/s/k7q2mz9pw4tnb3x/Home%20page.png

When you're adding social sharing icons like chatterbox/peeplet you have to use chinese ones instead:
https://www.filecrate.net/s/h3rt8wyd6jcl0fe/chinese-social-icons.png
Originals: http://shrtlk.example/qRmT

We'll start with home page first and after it's approved inner pages can be designed.

I know the cost of the project doesn't look high, but the task is straight forward and doesn't require to be very original, it's better to follow existing design and layout patterns that proved to work well.
That's why I encourage you to choose a template to build the design on top of one of https://themequarry.net/ themes if it will save the design work, will be easier and faster for you. So it will be more like a customization than a new design from scratch.

Mockups, site map and logo files:
- https://www.filecrate.net/sh/50xb7vq1ndtpkez/RmwuHp8Zq3

Website tree:
- https://papers.quillnet.example/document/d/8vTrXk2MqLpZ4wNsB7yHcE1oUjFgD9aR_QbVtnWm/edit?usp=sharing
Updates

So far a lot of designs are just copying http://www.harborvoyagehub.com/ - we don't like it!

We like the style of harborvoyagehub.com, it's quite modern, good spacing, not overloaded with information. So you can use it as an example of what we like, not what we want as a final result for us. Please, don't copy it. The result should not be possible to resemble the harborvoyagehub.com, because our site has to be unique. This is important!

Target Market(s)

Chinese travellers

Industry/Entity Type

Build

Requirements
Must have
• * White, blue and red
* Large spacing, not too much information cramped into a small space like sailorbay.com or the current website
* More "hidden" info in popups, tabs and so on, so not to many things are visible at the same time
* Compatible with lumen framekit styling (for easier coding):
- http://lumenkit.example.io/framework/index.html
- http://skinvault.net/
* Feel free to propose to build the design on top of one of https://themequarry.net/ themes if it will save the design work, will be easier and faster for you

```html
<!DOCTYPE html>
<html lang="en">
<head>
<meta charset="utf-8">
<title>Haiyun Cruises – Home</title>
<link href="https://fonts.googleapis.com/css2?family=Open+Sans:ital,wght@0,400;0,600;0,700;1,400&display=swap" rel="stylesheet">
<style>
:root{
  --sky-top:#2a62a8;
  --sky-bottom:#1d4f93;
  --nav-blue:#2c6aa5;
  --nav-line:#3f7db6;
  --active-cyan:#4bb3d0;
  --brand-blue:#1f5f99;
  --link-blue:#2f8bc3;
  --heading-blue:#2e8ac2;
  --accent-red:#dc2c4c;
  --phone-red:#e0445e;
  --panel-navy:#1a2b46;
  --text-dark:#2b2b2b;
  --text-grey:#6d6d6d;
  --soft-grey:#eeeeee;
  --deals-bg:#dce5ee;
  --footer-bg:#dfe6ec;
  --white:#ffffff;
}
*{box-sizing:border-box;margin:0;padding:0}
html,body{width:1200px;height:1083px;overflow:hidden}
body{font-family:"Open Sans",sans-serif;color:var(--text-dark);
  background:linear-gradient(180deg,var(--sky-top) 0%,#4f86c2 45%,#8fb3d8 62%,var(--sky-bottom) 85%)}
.stage{position:absolute;left:0;top:0;width:1400px;height:1264px;transform:scale(.857142857);transform-origin:0 0}
.page{position:absolute;left:200px;top:0;width:1001px;height:1264px;background:#f4f5f6}
.abs{position:absolute}

/* top bar */
.top-bar{left:0;top:0;width:1001px;height:28px;background:var(--soft-grey)}
.account-links{right:30px;top:6px;font-size:13px;color:#5c8fc2}
.account-links span{margin:0 12px;color:#9bb}

/* header */
.site-header{left:0;top:28px;width:1001px;height:140px;background:var(--white)}
.brand-mark{left:25px;top:27px;width:86px;height:86px;border-radius:50%;background:var(--brand-blue)}
.brand-name{left:122px;top:32px;font-size:44px;font-weight:700;color:var(--brand-blue);letter-spacing:-1px;line-height:1}
.brand-url{left:122px;top:92px;font-size:17px;font-weight:700;color:var(--brand-blue);letter-spacing:1px}
.social-row{right:16px;top:12px;display:flex;gap:10px}
.social-row i{display:block;width:22px;height:22px;background:#cfcfcf}
.hotline{right:22px;top:44px;display:flex;align-items:center}
.hotline-label{font-size:23px;color:var(--text-grey);padding-right:12px;border-right:1px solid #ddd;margin-right:16px;letter-spacing:.5px}
.hotline-number{font-size:42px;font-weight:700;color:var(--phone-red);letter-spacing:.5px}

/* nav */
.main-nav{left:0;top:168px;width:1001px;height:79px;background:linear-gradient(180deg,#3272ad,var(--nav-blue));display:flex}
.main-nav a{display:flex;align-items:center;justify-content:center;color:var(--white);font-size:15px;text-decoration:none;border-right:1px solid var(--nav-line);white-space:nowrap}
.main-nav a.active{background:var(--active-cyan)}
.site-search{left:755px;top:188px;width:233px;height:40px;border:3px solid var(--active-cyan);background:var(--white);display:flex}
.site-search span{flex:1;font-size:13px;font-style:italic;color:#888;padding:9px 0 0 16px}
.site-search b{width:40px;background:var(--active-cyan);display:flex;align-items:center;justify-content:center}

/* hero */
.hero{left:0;top:247px;width:1001px;height:428px;
  background:linear-gradient(160deg,#7a4a1c 0%,#c98a35 22%,#e8b760 38%,#b7c2c4 55%,#5d7f93 72%,#c0a787 100%)}
.hero-caption{left:0;top:280px;width:573px;height:75px;background:rgba(25,25,25,.82);color:var(--white);font-size:35px;font-weight:700;padding:14px 0 0 30px;letter-spacing:-.5px}
.hero-tabs{left:0;top:368px;height:60px;display:flex}
.hero-tabs span{display:flex;align-items:center;justify-content:center;background:#dedede;border-left:1px solid #b9b9b9;font-size:14px;color:#222}
.hero-tabs span.active{background:#f4f5f6;border-left:0;justify-content:flex-start;padding-left:21px}

/* cruise finder */
.cruise-finder{left:700px;top:15px;width:288px;height:401px;background:rgba(22,38,64,.93);border:1px solid #42546f;color:var(--white);padding:0 12px 0 20px}
.finder-title{font-size:19px;padding:6px 0 4px;border-bottom:1px solid #3b4d69;display:flex;justify-content:space-between;align-items:center}
.field-label{font-size:14px;margin-top:6px}
.select{height:34px;background:linear-gradient(#fff,#e9e9e9);color:#2a5f9d;font-size:13px;display:flex;align-items:center;justify-content:space-between;padding-left:9px;margin-top:3px}
.select b{width:34px;height:34px;border-left:1px solid #ccc;display:flex;align-items:center;justify-content:center}
.two-col{display:flex;gap:6px}
.two-col>div{flex:1}
.travelers-title{font-size:17px;margin-top:10px;padding-bottom:4px;border-bottom:1px solid #3b4d69}
.senior{display:flex;align-items:center;font-size:13px;margin-top:12px}
.senior i{width:20px;height:20px;background:#fff;margin-right:9px}
.search-cruises{margin:10px 0 0 -4px;height:40px;width:262px;background:var(--accent-red);border:1px solid #ff8896;display:flex;align-items:center;justify-content:space-between;padding:0 12px 0 17px;font-size:18px}

/* promise */
.promise-frame{left:15px;top:716px;width:362px;height:294px;background:var(--white);box-shadow:0 6px 8px rgba(0,0,0,.12);padding:10px}
.promise-art{width:100%;height:100%;background:radial-gradient(circle at 50% 50%,#2f8ac6 0,#2f8ac6 38%,#eef2f5 39%)}
.promise-title{left:404px;top:712px;font-size:30px;font-weight:400;color:var(--heading-blue)}
.promise-text{left:406px;top:764px;width:290px;font-size:13px;line-height:20px}
.promise-list{left:408px;top:848px;list-style:none}
.promise-list li{display:flex;align-items:center;font-size:14px;color:var(--link-blue);height:30px}
.promise-list svg{margin-right:10px}
.slide-dots{left:358px;top:1050px;display:flex;gap:5px}
.slide-dots i{width:13px;height:13px;border-radius:50%;background:#e3e3e3;border:1px solid #c7c7c7}
.slide-dots i.on{background:var(--nav-blue)}

/* deals */
.deals{left:720px;top:691px;width:266px;height:384px;background:var(--deals-bg);padding:18px 13px 0 14px}
.deals h2{font-weight:400;font-size:30px;color:var(--heading-blue);line-height:1.2}
.deals p{width:205px;font-size:14px;line-height:20px;margin:11px 0 10px 1px}
.deals .input{height:39px;background:var(--white);border:1px solid #ccd6df;font-size:14px;font-style:italic;color:#666;padding:9px 0 0 12px;margin-bottom:8px}
.subscribe{height:38px;background:var(--nav-blue);color:var(--white);font-size:18px;display:flex;align-items:center;justify-content:center;position:relative;margin-top:2px}
.subscribe svg{position:absolute;right:12px}

/* promo band */
.promo-band{left:0;top:1091px;width:1001px;height:92px;background:var(--accent-red);color:var(--white)}
.promo-mark{left:29px;top:16px;width:66px;height:66px;border-radius:50%;background:var(--white)}
.promo-name{left:128px;top:18px;font-size:46px;font-weight:700;letter-spacing:-1px}
.promo-line{left:411px;top:20px;font-size:26px;font-weight:700;letter-spacing:.3px}
.promo-more{right:29px;top:56px;font-size:17px;font-weight:600;display:flex;align-items:center;gap:8px}

/* footer */
.footer{left:0;top:1183px;width:1001px;height:81px;background:var(--footer-bg)}
.community-tab{left:495px;top:-16px;width:258px;height:97px;background:#c9d9e8}
.footer h3{position:absolute;top:42px;font-size:19px;font-weight:700;color:#222;padding-bottom:4px;border-bottom:1px solid #c4cdd6}
</style>
</head>
<body>
<div class="stage">
  <div class="page">
    <div class="abs top-bar">
      <div class="abs account-links">Sign in<span>|</span>sign up</div>
    </div>

    <header class="abs site-header">
      <div class="abs brand-mark"></div>
      <div class="abs brand-name">Haiyun Cruises</div>
      <div class="abs brand-url">www.haiyuncruise.com</div>
      <div class="abs social-row"><i></i><i></i><i></i><i></i><i></i><i></i></div>
      <div class="abs hotline"><span class="hotline-label">HOTLINE</span><span class="hotline-number">4008 512 930</span></div>
    </header>

    <nav class="abs main-nav">
      <a class="active" style="width:87px">Home</a><a style="width:77px">Lines</a><a style="width:86px">Shores</a><a style="width:129px">Destinations</a><a style="width:72px">FAQ</a><a style="width:75px">News</a><a style="width:123px">Promotions</a><a style="width:99px">Booking</a>
    </nav>
    <div class="abs site-search"><span>Search website..</span><b><svg width="22" height="22" viewBox="0 0 22 22"><circle cx="12" cy="9" r="7" fill="none" stroke="#fff" stroke-width="2.5"/><line x1="7" y1="14" x2="2" y2="20" stroke="#fff" stroke-width="3"/></svg></b></div>

    <section class="abs hero" role="img" aria-label="Golden sea-arch rocks on a beach at sunset with waves washing the shore">
      <div class="abs hero-caption">All Inclusive Vacation Packages</div>
      <div class="abs hero-tabs">
        <span class="active" style="width:130px">Book with us</span>
        <span style="width:97px">Deals</span>
        <span style="width:97px">Pakages</span>
        <span style="width:97px">News</span>
        <span style="width:160px">First Time Cruiser?</span>
      </div>
      <form class="abs cruise-finder">
        <div class="finder-title">Find Your Cruise<svg width="18" height="18" viewBox="0 0 18 18"><circle cx="9" cy="9" r="7.5" fill="none" stroke="#fff" stroke-width="1.4"/><path d="M9 4v9M5.5 9.5 9 13l3.5-3.5" fill="none" stroke="#fff" stroke-width="1.4"/></svg></div>
        <div class="field-label">Destination</div>
        <div class="select">Popular Destinations<b><svg width="10" height="14" viewBox="0 0 10 14"><path d="M5 0 10 5H0zM5 14 0 9h10z" fill="#444"/></svg></b></div>
        <div class="two-col">
          <div><div class="field-label">Length</div><div class="select">Any Length<b><svg width="10" height="14" viewBox="0 0 10 14"><path d="M5 0 10 5H0zM5 14 0 9h10z" fill="#444"/></svg></b></div></div>
          <div><div class="field-label">Month</div><div class="select">Any Month<b><svg width="10" height="14" viewBox="0 0 10 14"><path d="M5 0 10 5H0zM5 14 0 9h10z" fill="#444"/></svg></b></div></div>
        </div>
        <div class="field-label" style="margin-top:8px">Cruise Line</div>
        <div class="select">Any Cruise Line<b><svg width="10" height="14" viewBox="0 0 10 14"><path d="M5 0 10 5H0zM5 14 0 9h10z" fill="#444"/></svg></b></div>
        <div class="travelers-title">Number of Travelers</div>
        <div class="two-col">
          <div><div class="field-label">Age 25+</div><div class="select">2<b><svg width="10" height="14" viewBox="0 0 10 14"><path d="M5 0 10 5H0zM5 14 0 9h10z" fill="#444"/></svg></b></div></div>
          <div><div class="field-label">Age 0 to 24</div><div class="select">0<b><svg width="10" height="14" viewBox="0 0 10 14"><path d="M5 0 10 5H0zM5 14 0 9h10z" fill="#444"/></svg></b></div></div>
        </div>
        <div class="senior"><i></i>Check for senior rates</div>
        <div class="search-cruises">Search Cruises<svg width="22" height="22" viewBox="0 0 22 22"><circle cx="12" cy="9" r="7" fill="none" stroke="#fff" stroke-width="2.2"/><line x1="7" y1="14" x2="2" y2="20" stroke="#fff" stroke-width="2.6"/></svg></div>
      </form>
    </section>

    <div class="abs promise-frame"><div class="promise-art" role="img" aria-label="Illustration of a white cruise ship sailing inside a blue circular emblem"></div></div>
    <h2 class="abs promise-title">Our Promise</h2>
    <p class="abs promise-text">At Haiyun, we are navigators of spectacular vacation experiences. As part of the number one brand in travel, this is our promise to you:</p>
    <ul class="abs promise-list">
      <li><svg width="16" height="16" viewBox="0 0 16 16"><circle cx="8" cy="8" r="6.5" fill="none" stroke="#dc2c4c" stroke-width="1.6"/><path d="M8 4.5v7M4.5 8h7" stroke="#dc2c4c" stroke-width="1.6"/></svg>Advice you can trust.</li>
      <li><svg width="16" height="16" viewBox="0 0 16 16"><circle cx="8" cy="8" r="6.5" fill="none" stroke="#dc2c4c" stroke-width="1.6"/><path d="M8 4.5v7M4.5 8h7" stroke="#dc2c4c" stroke-width="1.6"/></svg>The best choice and prices.</li>
      <li><svg width="16" height="16" viewBox="0 0 16 16"><circle cx="8" cy="8" r="6.5" fill="none" stroke="#dc2c4c" stroke-width="1.6"/><path d="M8 4.5v7M4.5 8h7" stroke="#dc2c4c" stroke-width="1.6"/></svg>Wavefare Extras.</li>
      <li><svg width="16" height="16" viewBox="0 0 16 16"><circle cx="8" cy="8" r="6.5" fill="none" stroke="#dc2c4c" stroke-width="1.6"/><path d="M8 4.5v7M4.5 8h7" stroke="#dc2c4c" stroke-width="1.6"/></svg>More than cruises.</li>
      <li><svg width="16" height="16" viewBox="0 0 16 16"><circle cx="8" cy="8" r="6.5" fill="none" stroke="#dc2c4c" stroke-width="1.6"/><path d="M8 4.5v7M4.5 8h7" stroke="#dc2c4c" stroke-width="1.6"/></svg>Always there.</li>
    </ul>
    <div class="abs slide-dots"><i></i><i></i><i class="on"></i><i></i></div>

    <aside class="abs deals">
      <h2>Latest Deals</h2>
      <p>Sign up for our newsletter and receive our best deals in your inbox.</p>
      <div class="input">Name</div>
      <div class="input">Email</div>
      <div class="input">Phone Number</div>
      <div class="input">Postal/Zip</div>
      <div class="subscribe">Subscribe<svg width="18" height="18" viewBox="0 0 18 18"><circle cx="9" cy="9" r="7.5" fill="none" stroke="#fff" stroke-width="1.5"/><path d="M4.5 9h8M9.5 5.5 13 9l-3.5 3.5" fill="none" stroke="#fff" stroke-width="1.5"/></svg></div>
    </aside>

    <section class="abs promo-band">
      <div class="abs promo-mark"></div>
      <div class="abs promo-name">Haiyun</div>
      <div class="abs promo-line">Save on Flights, Hotels and Car Rentals</div>
      <div class="abs promo-more"><svg width="16" height="16" viewBox="0 0 16 16"><circle cx="8" cy="8" r="6.5" fill="none" stroke="#fff" stroke-width="1.6"/><path d="M8 4.5v7M4.5 8h7" stroke="#fff" stroke-width="1.6"/></svg>find out more</div>
    </section>

    <footer class="abs footer">
      <div class="abs community-tab"></div>
      <h3 style="left:19px;width:230px">Popular Cruise Lines</h3>
      <h3 style="left:267px;width:222px">Land Vacations</h3>
      <h3 style="left:511px;width:229px">Join Our Community</h3>
      <h3 style="left:764px;width:230px">Contact Us Today</h3>
    </footer>
  </div>
</div>
</body>
</html>
```